Design an Outstanding flyer for my company.

I need a flyer designed for our window tinting company based in Brisbane Queensland Australia. The flyer will be targeting Home tinting. We also do mobile car tinting. Something in regards to this could be incorporated into the flyer as well.
I want it to be 2 sided DL size. Black background.
It really needs to Pop, and be a real attention getter.
It needs to be easy to read.
I have provided a mock up with the info on it from our marketing company. It will need a spellcheck etc to make sure everything is correct.
Everything about it can be changed however you like.
I have also included the company logo.

Lets see what you've got!

Target Market(s)

Home Owners

Industry/Entity Type

Home Improvement

Font styles to use
Other font styles liked:
• Duan Penh

Requirements
Must have
• All the information on the mock up. Clear and easy to read.
• Must Stand Out!

```html
<!DOCTYPE html>
<html lang="en">
<head>
<meta charset="utf-8">
<title>BrightLine Window Tinting – DL Flyer</title>
<link href="https://fonts.googleapis.com/css2?family=Source+Sans+3:wght@600;700;800&display=swap" rel="stylesheet">
<style>
  :root {
    --ink: #232221;
    --yellow: #ffe81a;
    --gold: #f7c51e;
    --white: #ffffff;
    --paper: #ffffff;
  }
  * { box-sizing: border-box; margin: 0; padding: 0; }
  html, body { width: 1190px; height: 1200px; overflow: hidden; background: var(--paper); }
  body { position: relative; font-family: "Source Sans 3", "Myriad Pro", Arial, sans-serif; font-weight: 700; }

  .flyer {
    position: absolute; top: 56px; width: 518px; height: 1087px;
    background: var(--ink); overflow: hidden; text-align: center;
  }
  .flyer--front { left: 55px; }
  .flyer--back { left: 620px; }

  .band { position: absolute; left: 0; top: 0; width: 518px; height: 1087px; }
  .block { position: absolute; left: 0; width: 100%; }

  .headline { line-height: 1; letter-spacing: -0.5px; }
  .headline .big { display: block; font-size: 64px; font-weight: 800; }
  .headline .mid { display: block; font-size: 44px; margin-top: 6px; }
  .headline .huge { display: block; font-size: 72px; font-weight: 800; margin-top: 4px; }
  .flyer--front .headline { color: var(--yellow); top: 30px; }

  .privacy { color: var(--white); font-size: 40px; letter-spacing: -0.3px; top: 234px; }

  .benefits {
    color: var(--white); font-size: 12px; line-height: 20px;
    letter-spacing: -0.2px; padding: 0 44px;
  }
  .flyer--front .benefits { top: 290px; }
  .flyer--back .benefits { top: 578px; padding: 0 36px; line-height: 21px; }

  .reasons { font-size: 33px; line-height: 42px; letter-spacing: -0.4px; }
  .flyer--front .reasons { color: var(--ink); top: 522px; }
  .flyer--back .reasons { color: var(--white); font-size: 27px; line-height: 43px; top: 30px; }

  .flyer--back .headline { color: var(--ink); top: 238px; }
  .flyer--back .headline .big { font-size: 58px; }
  .flyer--back .headline .mid { font-size: 42px; margin-top: 4px; }
  .flyer--back .headline .huge { font-size: 69px; margin-top: 2px; }
  .flyer--back .headline .priv { display: block; font-size: 48px; margin-top: 4px; }

  .call { color: var(--gold); font-size: 19px; line-height: 27px; top: 745px; }
  .contact { color: var(--white); font-size: 26px; line-height: 31px; top: 818px; }

  .brand {
    top: 946px; display: flex; align-items: center; justify-content: center; gap: 12px;
  }
  .brand__dot { width: 46px; height: 46px; border-radius: 50%; background: var(--gold); flex: none; }
  .brand__name { color: var(--gold); font-size: 27px; line-height: 1; letter-spacing: 0.3px; white-space: nowrap; }

  .web { color: var(--white); font-size: 18px; top: 1046px; }
</style>
</head>
<body>

<section class="flyer flyer--front" aria-label="Flyer front">
  <svg class="band" viewBox="0 0 518 1087" aria-hidden="true">
    <defs>
      <linearGradient id="gold-front" x1="0" x2="1" y1="0" y2="0">
        <stop offset="0" stop-color="#f9c51c"/>
        <stop offset="0.2" stop-color="#ffee1a"/>
        <stop offset="0.65" stop-color="#f8c322"/>
        <stop offset="1" stop-color="#ffee1a"/>
      </linearGradient>
    </defs>
    <path d="M0,438 Q250,525 518,445 L518,604 Q470,658 420,670 Q220,712 0,716 Z" fill="var(--white)"/>
    <path d="M0,452 Q250,538 518,462 L518,590 Q470,644 420,656 Q220,700 0,704 Z" fill="url(#gold-front)"/>
  </svg>

  <h1 class="block headline">
    <span class="big">KEEP HEAT OUT</span>
    <span class="mid">BLOCK 99.9% UV RAYS</span>
    <span class="huge">SAVE MONEY</span>
  </h1>
  <p class="block privacy">INCREASE PRIVACY</p>
  <p class="block benefits">REDUCE GLARE. REDUCE ENERGY COSTS. CONTROL THE AMOUNT OF LIGHT ENTERING YOUR HOME. REDUCE CARBON FOOTPRINT. MAKE HOME MORE BEAUTIFUL. ELIMINATE HOME HOT SPOTS. PROTECT AGAINST BROKEN GLASS. REGULATE ENERGY. PROTECTS UPHOLSTERY. IMPROVE EFFECTIVENESS OF ROOF INSULATION. IMPROVE HEALTH. REDUCES INTERIOR FLOOR FADING. ELIMINATE NEED FOR BLINDS. STRENGTHEN YOUR WINDOWS. INSULATE IN WINTER. AFFORDABLE.</p>
  <h2 class="block reasons">20 REASONS WHY<br>HOME WINDOW TINTING<br>IS PERFECT FOR YOU.</h2>
  <p class="block call">CALL BRISBANE’S LEADER IN<br>HOME WINDOW TINTING NOW.</p>
  <p class="block contact">TEL: 07 3000 1188<br>SMS: 0400 555 219</p>
  <div class="block brand"><span class="brand__dot"></span><span class="brand__name">BrightLine Window Tinting</span></div>
  <p class="block web">www.brightlinetinting.com.au</p>
</section>

<section class="flyer flyer--back" aria-label="Flyer back">
  <svg class="band" viewBox="0 0 518 1087" aria-hidden="true">
    <defs>
      <linearGradient id="gold-back" x1="0" x2="1" y1="0" y2="0">
        <stop offset="0" stop-color="#ffee1a"/>
        <stop offset="0.55" stop-color="#ffe21a"/>
        <stop offset="0.8" stop-color="#f8c322"/>
        <stop offset="1" stop-color="#ffee1a"/>
      </linearGradient>
    </defs>
    <path d="M0,137 Q260,210 518,182 L518,478 Q300,545 0,548 Z" fill="var(--white)"/>
    <path d="M0,155 Q260,228 518,196 L518,468 Q300,532 0,535 Z" fill="url(#gold-back)"/>
  </svg>

  <h2 class="block reasons">20 REASONS WHY<br>HOME WINDOW TINTING<br>IS PERFECT FOR YOU.</h2>
  <h1 class="block headline">
    <span class="big">KEEP HEAT OUT</span>
    <span class="mid">BLOCK 99.9% UV RAYS</span>
    <span class="huge">SAVE MONEY</span>
    <span class="priv">INCREASE PRIVACY</span>
  </h1>
  <p class="block benefits">REDUCE GLARE. REDUCE ENERGY COSTS. CONTROL THE AMOUNT OF LIGHT ENTERING YOUR HOME. REDUCE CARBON FOOTPRINT. MAKE HOME MORE BEAUTIFUL. ELIMINATE HOME HOT SPOTS. PROTECT AGAINST BROKEN GLASS. REGULATE ENERGY. PROTECTS UPHOLSTERY. IMPROVE EFFECTIVENESS OF ROOF INSULATION. IMPROVE HEALTH. REDUCES INTERIOR FLOOR FADING. ELIMINATE NEED FOR BLINDS. STRENGTHEN YOUR WINDOWS. INSULATE IN WINTER. AFFORDABLE.</p>
  <p class="block call">CALL BRISBANE’S LEADER IN<br>HOME WINDOW TINTING NOW.</p>
  <p class="block contact">TEL: 07 3000 1188<br>SMS: 0400 555 219</p>
  <div class="block brand"><span class="brand__dot"></span><span class="brand__name">BrightLine Window Tinting</span></div>
  <p class="block web">www.brightlinetinting.com.au</p>
</section>

</body>
</html>
```